North Carolina-themed postcard

Would like 3x distinct designs for a postcard (sized 4.5 x 5.5) that celebrates the state of North Carolina. A vintage theme, a modern theme, and a simple black/white theme would be suggestions for design styles.

```html
<!DOCTYPE html>
<html lang="en">
<head>
<meta charset="utf-8">
<title>Greetings from North Carolina – Postcard</title>
<link rel="stylesheet" href="https://fonts.googleapis.com/css2?family=Dancing+Script:wght@700&family=Titan+One&family=Open+Sans:wght@700&display=swap">
<style>
  :root {
    --canvas: #d9d9d9;
    --card-edge: #1d1d1f;
    --sky-light: #eef7fc;
    --sky: #a9d4ef;
    --sky-deep: #3f8fcf;
    --orange: #f3a45e;
    --teal: #9fdcd0;
    --navy: #1f2a6b;
    --red: #d9323c;
    --shadow-red: #e8666c;
    --ink: #1a1a1a;
    --paper: #ffffff;
  }
  html, body {
    margin: 0;
    width: 1200px;
    height: 696px;
    overflow: hidden;
    background: var(--canvas);
  }
  .canvas { position: relative; width: 1200px; height: 696px; }
  .postcard {
    position: absolute;
    top: 150px;
    width: 560px;
    height: 396px;
    box-shadow: 0 3px 6px rgba(0,0,0,.25);
  }
  .postcard--back { left: 25px; }
  .postcard--front { left: 615px; }
  .postcard svg { display: block; width: 100%; height: 100%; }
  .greeting-script { font-family: "Dancing Script", cursive; font-weight: 700; }
  .state-letters { font-family: "Titan One", sans-serif; }
  .caption { font-family: "Open Sans", sans-serif; font-weight: 700; }
</style>
</head>
<body>
<main class="canvas">

  <section class="postcard postcard--back">
    <svg viewBox="0 0 560 396" xmlns="http://www.w3.org/2000/svg">
      <defs>
        <linearGradient id="backWash" x1="0" y1="0" x2="1" y2="1">
          <stop offset="0" stop-color="#f4f4f4"/>
          <stop offset="0.5" stop-color="#e9e9e9"/>
          <stop offset="1" stop-color="#f2f2f2"/>
        </linearGradient>
      </defs>
      <rect class="card-paper" width="560" height="396" fill="var(--paper)"/>
      <rect class="capitol-watermark" role="img" aria-label="Faint grey photograph of the State Capitol building with statue"
            width="560" height="396" fill="url(#backWash)"/>
      <line class="divider" x1="290" y1="40" x2="270" y2="360" stroke="var(--ink)" stroke-width="1"/>
      <rect class="stamp-box" x="470" y="50" width="80" height="55" fill="none" stroke="var(--ink)" stroke-width="1.2"/>
      <g class="address-lines" stroke="var(--ink)" stroke-width="1">
        <line x1="300" y1="170" x2="540" y2="178"/>
        <line x1="298" y1="205" x2="538" y2="213"/>
        <line x1="296" y1="240" x2="536" y2="248"/>
        <line x1="294" y1="275" x2="534" y2="283"/>
      </g>
      <rect class="card-edge" x="0.5" y="0.5" width="559" height="395" fill="none" stroke="#bdbdbd"/>
    </svg>
  </section>

  <section class="postcard postcard--front">
    <svg viewBox="0 0 560 396" xmlns="http://www.w3.org/2000/svg">
      <defs>
        <radialGradient id="skyWash" cx="0.35" cy="0.6" r="0.8">
          <stop offset="0" stop-color="var(--sky-light)"/>
          <stop offset="0.55" stop-color="var(--sky)"/>
          <stop offset="1" stop-color="var(--sky-deep)"/>
        </radialGradient>
        <linearGradient id="cityFill" x1="0" y1="0" x2="0.3" y2="1">
          <stop offset="0" stop-color="#6fa3d6"/>
          <stop offset="0.35" stop-color="#9bb4c9"/>
          <stop offset="0.6" stop-color="#b08a5a"/>
          <stop offset="1" stop-color="#3f7a3c"/>
        </linearGradient>
        <radialGradient id="blossom" cx="0.5" cy="0.45" r="0.55">
          <stop offset="0" stop-color="#ffffff"/>
          <stop offset="0.6" stop-color="#e8f1ec"/>
          <stop offset="1" stop-color="#9cc79a" stop-opacity="0"/>
        </radialGradient>
        <radialGradient id="capitolFill" cx="0.5" cy="0.5" r="0.6">
          <stop offset="0" stop-color="#e3c98a"/>
          <stop offset="0.6" stop-color="#c9b27f"/>
          <stop offset="1" stop-color="#b9d7ec" stop-opacity="0"/>
        </radialGradient>
        <path id="arcNorth" d="M55 245 Q 190 160 335 175"/>
        <path id="arcCarolina" d="M130 300 Q 320 215 515 210"/>
      </defs>

      <rect class="card-base" width="560" height="396" fill="url(#skyWash)"/>

      <g class="brush-strokes">
        <polygon class="brush brush--orange" points="300,0 560,0 560,250 520,200 470,90 380,40" fill="var(--orange)" opacity=".9"/>
        <polygon class="brush brush--blue" points="160,0 330,0 360,30 300,45 200,25" fill="var(--sky-deep)" opacity=".75"/>
        <polygon class="brush brush--teal" points="330,10 450,0 490,90 470,120 400,60" fill="var(--teal)" opacity=".7"/>
        <polygon class="brush brush--blue-low" points="0,270 30,260 40,396 0,396" fill="var(--sky-deep)" opacity=".7"/>
        <rect class="halftone-patch" role="img" aria-label="Yellow halftone dot pattern" x="490" y="0" width="70" height="150" fill="#e9e36a" opacity=".55"/>
      </g>

      <rect class="inner-frame" x="14" y="14" width="532" height="368" fill="none" stroke="var(--ink)" stroke-width="1"/>

      <text class="greeting-script" x="55" y="112" font-size="38" transform="rotate(-10 55 112)"
            fill="var(--navy)" stroke="#fff" stroke-width="3" paint-order="stroke">Greetings <tspan fill="var(--red)">from</tspan></text>

      <g class="state-name" role="img" aria-label="North Carolina lettering filled with city photographs">
        <text class="state-letters" font-size="58" fill="var(--shadow-red)" stroke="#fff" stroke-width="3" paint-order="stroke" transform="translate(3 6)">
          <textPath href="#arcNorth" textLength="285" lengthAdjust="spacingAndGlyphs">NORTH</textPath>
        </text>
        <text class="state-letters" font-size="58" fill="url(#cityFill)" stroke="#fff" stroke-width="2.5" paint-order="stroke">
          <textPath href="#arcNorth" textLength="285" lengthAdjust="spacingAndGlyphs">NORTH</textPath>
        </text>
        <text class="state-letters" font-size="56" fill="var(--shadow-red)" stroke="#fff" stroke-width="3" paint-order="stroke" transform="translate(3 6)">
          <textPath href="#arcCarolina" textLength="385" lengthAdjust="spacingAndGlyphs">CAROLINA</textPath>
        </text>
        <text class="state-letters" font-size="56" fill="url(#cityFill)" stroke="#fff" stroke-width="2.5" paint-order="stroke">
          <textPath href="#arcCarolina" textLength="385" lengthAdjust="spacingAndGlyphs">CAROLINA</textPath>
        </text>
      </g>

      <ellipse class="dogwood-photo" role="img" aria-label="Photograph of a white dogwood blossom with green leaves"
               cx="265" cy="340" rx="95" ry="50" fill="url(#blossom)"/>

      <text class="caption" x="400" y="268" font-size="12" fill="var(--ink)" transform="rotate(-12 400 268)">State Capitol In Raleigh</text>
      <ellipse class="capitol-photo" role="img" aria-label="Photograph of the State Capitol in Raleigh with statue in front"
               cx="468" cy="318" rx="78" ry="50" fill="url(#capitolFill)"/>

      <rect class="card-edge" x="1.5" y="1.5" width="557" height="393" fill="none" stroke="var(--card-edge)" stroke-width="3"/>
    </svg>
  </section>

</main>
</body>
</html>
```